Venture Backed Startup Company for SaaS Lead Generation ***Guaranteed Payment and Fast Feedback***

***Guaranteed Payment***
***I Give Fast Feedback***

I need a one-page website design for a startup company. We sell lead generation and appointment setting services to B2B SaaS companies.

Looking for a clean, modern, flat, "Saas-style" design. A simple but trustworthy and authoritative color palette is best. Pictures of actual people are very good to use too

Here are some websites I like and the reasons why:

https://www.pellarin.com - simple and intuitive design, very clear, strong CTA, explains the process succinctly, and has pics of people/faces\

https://www.tovemark.com/ - clean and simple, flat design, strong CTA, easy to understand

https://www.quorvel.io/ - simple and clean navigation, easy to understand what to do next

https://brisketfolder.com/ - strong step by step approach, easy to understand the value of the website, clean and sharp design

https://pinwardle.com/ - Great color scheme, clean, easy to read, great font

Target Market(s)

startups, entrepeneur, B2B SaaS

Industry/Entity Type

SaaS

Number of Pages Required

1 page

Font styles to use
Sans Serif

Colors

Designer to choose colors to be used in the design.

Requirements
Must have
• Good graphics, a theme, and pictures of people
Nice to have
• Here are other websites like and the reason why
• https://marqueloft.com/ - Great graphics, clean and flat design, pictures of people, modern design
• https://dunvelio.com/ - Clean, pictures of people, easy to read, good contrast
• https://yarrowpeak.co/ -- Good graphics and great font, easy to read, great color scheme
• http://tillerandvane.com/ - clean design

```html
<!DOCTYPE html>
<html lang="en">
<head>
<meta charset="utf-8">
<title>Halvern – Lead Generation</title>
<link rel="stylesheet" href="https://fonts.googleapis.com/css2?family=Open+Sans:wght@400;600;700&family=Roboto+Condensed:wght@400;700&display=swap">
<style>
:root{
  --navy:#0d1b3e;
  --navy-deep:#081330;
  --blue:#1e6fb8;
  --accent:#d9a441;
  --ink:#222;
  --muted:#666;
  --white:#fff;
}
*{box-sizing:border-box;margin:0;padding:0}
html,body{width:1200px;height:4138px;overflow:hidden}
body{position:relative;background:var(--white);font-family:"Open Sans",Arial,sans-serif;color:var(--ink)}
.abs{position:absolute}
/* header */
.site-header{position:absolute;left:0;top:0;width:1200px;height:118px;background:var(--white)}
.brand{position:absolute;left:88px;top:36px;font-family:"Roboto Condensed",Arial,sans-serif;font-weight:700;font-size:40px;letter-spacing:1px;color:var(--navy)}
.main-nav{position:absolute;right:90px;top:48px;display:flex;gap:40px;font-size:15px;color:var(--ink);align-items:center}
.main-nav .active{color:var(--blue)}
/* hero */
.hero{position:absolute;left:0;top:118px;width:1200px;height:607px;background:radial-gradient(circle at 75% 30%,#1f3a72 0%,var(--navy) 45%,var(--navy-deep) 100%)}
.hero-art{position:absolute;left:70px;top:70px;width:570px;height:400px;border-radius:6px;background:linear-gradient(135deg,#2d4d8f,#3b6fc0 60%,#1b3266)}
.hero-title{position:absolute;left:655px;top:195px;font-family:"Roboto Condensed",Arial,sans-serif;font-weight:400;font-size:66px;line-height:80px;color:var(--white)}
.hero-sub{position:absolute;left:657px;top:282px;font-family:"Roboto Condensed",Arial,sans-serif;font-weight:400;font-size:32px;color:var(--white)}
.hero-dots{position:absolute;left:1158px;top:225px;display:flex;flex-direction:column;gap:14px}
.hero-dots span{width:8px;height:8px;border-radius:50%;background:var(--white)}
/* welcome */
.welcome-frame{position:absolute;left:100px;top:840px;width:355px;height:250px;border:1px solid #444}
.welcome-art{position:absolute;left:125px;top:862px;width:380px;height:333px;background:linear-gradient(135deg,#2e5fb0,#1d3f85)}
.welcome-title{position:absolute;left:558px;top:882px;font-size:42px;font-weight:400;color:var(--ink)}
.welcome-title b{color:var(--blue);font-weight:400}
.welcome-text{position:absolute;left:558px;top:952px;width:545px;font-size:14.5px;line-height:29px;color:var(--muted)}
.btn-small{position:absolute;left:562px;top:1137px;padding:4px 16px;border-radius:14px;background:var(--blue);color:var(--white);font-size:13px}
/* services */
.services{position:absolute;left:0;top:1308px;width:1200px;height:642px;background:radial-gradient(circle at 60% 70%,#2f6aa8 0%,#15366a 40%,var(--navy-deep) 100%)}
.section-title{position:absolute;left:0;width:1200px;text-align:center;font-size:40px;font-weight:400}
.services .section-title{top:60px;color:var(--white)}
.service-card{position:absolute;top:217px;width:240px;height:255px;background:var(--white);text-align:center;padding:62px 16px 0}
.service-card h3{font-size:16px;font-weight:600;margin-bottom:12px}
.service-card p{font-size:12.5px;line-height:18px;color:var(--muted)}
.read-more{display:inline-block;margin-top:14px;font-size:13px;font-weight:600;color:var(--ink);padding-bottom:5px;border-bottom:2px solid var(--accent)}
.service-icon{position:absolute;top:-38px;left:50%;margin-left:-40px;width:80px;height:80px;border-radius:50%;background:var(--blue);border:4px solid var(--white);display:flex;align-items:center;justify-content:center}
/* projects */
.project-card{position:absolute;top:2150px;width:498px;height:420px;background:var(--white);box-shadow:0 1px 6px rgba(0,0,0,.2)}
.project-img{height:235px}
.project-card h3{margin:30px 0 0 38px;font-size:20px;font-weight:400}
.project-card p{margin:12px 38px 0;font-size:13px;line-height:20px;color:var(--muted)}
.project-card .read-more{margin:18px 0 0 38px;font-size:12.5px}
/* testimonial */
.testimonial{position:absolute;left:0;top:2690px;width:1200px;height:510px;background:radial-gradient(circle at 60% 50%,#2f6fc0 0%,#1a4a95 50%,#0f2d66 100%)}
.testimonial .section-title{top:65px;color:var(--white)}
.quote-box{position:absolute;left:250px;top:165px;width:740px;height:190px;border:2px solid var(--white);padding:28px 30px 0 110px;color:var(--white);font-size:14px;line-height:25px}
.quote-box .mark{position:absolute;left:78px;top:18px;font-size:40px;font-weight:700;line-height:1}
.quote-box cite{display:block;font-style:italic}
.avatar{position:absolute;left:175px;top:2882px;width:140px;height:140px;border-radius:50%;background:linear-gradient(135deg,#c9ced8,#6b7894);border:4px solid var(--white)}
.arrows{position:absolute;left:922px;top:3072px}
/* blog */
.blog-card{position:absolute;top:3380px;width:312px}
.blog-img{height:172px}
.blog-meta{display:flex;margin-top:12px;font-size:11px;color:var(--white);height:18px}
.blog-meta span{padding:2px 10px;background:var(--navy);display:flex;align-items:center}
.blog-meta span+span{background:#444}
.blog-card h3{margin-top:16px;font-size:16px;font-weight:400}
.blog-card p{margin-top:6px;font-size:12.5px;line-height:17px;color:var(--muted)}
.blog-card .more{display:block;margin-top:10px;font-size:12px;color:var(--blue)}
/* footer */
.footer-brand{position:absolute;left:88px;top:3946px;font-family:"Roboto Condensed",Arial,sans-serif;font-weight:700;font-size:40px;color:var(--white)}
.social{position:absolute;left:962px;top:3848px;display:flex;gap:12px}
.social span{width:26px;height:26px;border-radius:3px;background:#bdbdbd}
.newsletter-label{position:absolute;left:612px;top:3963px;font-size:15px;color:var(--white)}
.newsletter{position:absolute;left:828px;top:3950px;width:280px;height:46px;border:2px solid var(--white);border-radius:23px;padding:12px 20px;font-size:13px;color:#aaa}
.newsletter i{position:absolute;right:12px;top:11px;width:20px;height:20px;border-radius:50%;background:var(--white)}
.footer-nav{position:absolute;left:90px;top:4068px;display:flex;gap:30px;font-size:14px;color:var(--white)}
.copyright{position:absolute;right:105px;top:4070px;font-size:13px;color:var(--white)}
</style>
</head>
<body>

<header class="site-header">
  <div class="brand">HALVERN</div>
  <nav class="main-nav">
    <span class="active">HOME</span><span>ABOUT US</span><span>SERVICES</span><span>PROJECT</span><span>BLOG</span><span>CONTACT</span>
    <svg width="18" height="18" viewBox="0 0 18 18"><circle cx="7.5" cy="7.5" r="5.5" fill="none" stroke="#222" stroke-width="2.5"/><line x1="11.5" y1="11.5" x2="16" y2="16" stroke="#222" stroke-width="3"/></svg>
  </nav>
</header>

<section class="hero">
  <div class="hero-art" role="img" aria-label="Flat illustration of a sales funnel feeding leads into a laptop with a magnifying glass and charts"></div>
  <h1 class="hero-title">Lead Generation</h1>
  <p class="hero-sub">And appointment setting services</p>
  <div class="hero-dots"><span></span><span></span><span></span><span></span></div>
</section>
<svg class="abs" style="left:0;top:600px" width="1200" height="130" viewBox="0 0 1200 130">
  <polygon points="0,125 0,100 1200,20 1200,125" fill="#1e6fb8"/>
  <polygon points="0,125 0,115 640,82 1200,125" fill="#fff"/>
</svg>

<div class="welcome-frame"></div>
<div class="welcome-art" role="img" aria-label="Flat illustration of a lead funnel above a laptop with a magnifying glass"></div>
<h2 class="welcome-title">Welcome to <b>Halvern</b></h2>
<p class="welcome-text">It is a long established fact that a reader will be distracted by the readable content of a page when looking at its layout. The point of using Lorem Ipsum is that it has a more-or-less normal distribution of letters, as opposed to using 'Content here, content here', making it look like readable English. Many desktop publishing packages It is a long established fact that a reader will be distracted by the readable content of a page</p>
<span class="btn-small">Read More</span>

<section class="services">
  <h2 class="section-title">Our Services</h2>
  <div class="service-card" style="left:92px">
    <div class="service-icon"><svg width="30" height="30" viewBox="0 0 30 30"><circle cx="15" cy="15" r="10" fill="none" stroke="#fff" stroke-width="5" stroke-dasharray="4 3"/><circle cx="15" cy="15" r="4" fill="#fff"/></svg></div>
    <h3>Lead Generation</h3>
    <p>It is a long established fact that a reader will be is tracted by the readable content of a page when looking</p>
    <span class="read-more">READ MORE</span>
  </div>
  <div class="service-card" style="left:352px">
    <div class="service-icon"><svg width="26" height="30" viewBox="0 0 26 30"><path d="M2 1h15l7 7v21H2z" fill="#fff"/><path d="M7 13h12M7 18h12M7 23h8" stroke="#1e6fb8" stroke-width="2"/></svg></div>
    <h3>Appointment Setting</h3>
    <p>It is a long established fact that a reader will be is tracted by the readable content of a page when looking</p>
    <span class="read-more">READ MORE</span>
  </div>
  <div class="service-card" style="left:614px">
    <div class="service-icon"><svg width="32" height="28" viewBox="0 0 32 28"><rect x="2" y="2" width="28" height="18" fill="none" stroke="#fff" stroke-width="3"/><path d="M10 26h12M16 20v6" stroke="#fff" stroke-width="3"/></svg></div>
    <h3>Conversion Tracking</h3>
    <p>It is a long established fact that a reader will be is tracted by the readable content of a page when looking</p>
    <span class="read-more">READ MORE</span>
  </div>
  <div class="service-card" style="left:875px">
    <div class="service-icon"><svg width="30" height="30" viewBox="0 0 30 30"><polygon points="28,2 2,14 12,17 15,28" fill="#fff"/></svg></div>
    <h3>Contact Targeting</h3>
    <p>It is a long established fact that a reader will be is tracted by the readable content of a page when looking</p>
    <span class="read-more">READ MORE</span>
  </div>
</section>
<svg class="abs" style="left:0;top:1860px" width="1200" height="95" viewBox="0 0 1200 95">
  <polygon points="0,0 1200,90 1200,95 0,95" fill="#111"/>
  <polygon points="0,95 1200,60 1200,95" fill="#fff"/>
</svg>

<h2 class="section-title" style="top:2052px">Our Projects</h2>
<article class="project-card" style="left:92px">
  <div class="project-img" role="img" aria-label="Photo of a businessman touching floating finance and idea icons" style="background:linear-gradient(135deg,#2c4f6e,#6f93a8 50%,#1d3347)"></div>
  <h3>Neque porro quisquam est qui</h3>
  <p>Praesent elementum elit at tellus nec ultricies sit amet porttitor mattis enim In massa libero interdum nec interdum vel blandit</p>
  <span class="read-more">READ MORE</span>
</article>
<article class="project-card" style="left:612px">
  <div class="project-img" role="img" aria-label="Photo of a businessman pushing a large lead generation wheel beside a rising arrow" style="background:linear-gradient(135deg,#c9dcee,#8fb4d8 50%,#3f7fc0)"></div>
  <h3>Dolorem ipsum quia dolor sit amet</h3>
  <p>Praesent elementum elit at tellus nec ultricies sit amet porttitor mattis enim In massa libero interdum nec interdum</p>
  <span class="read-more">READ MORE</span>
</article>

<section class="testimonial">
  <h2 class="section-title">Testimonial</h2>
  <div class="quote-box">
    <span class="mark">“</span>
    The point of using Lorem Ipsum is that it has a more-or-less normal distribution of letters, as opposed to using 'Content here, content here', making it look like readable English. Many desktop publishing packages and web page editors now use Lorem Ipsum as their default model text, and a search for 'lorem ipsum' will uncover many
    <cite>- porro quisquam</cite>
  </div>
</section>
<svg class="arrows" width="66" height="14" viewBox="0 0 66 14">
  <path d="M2 7h24M2 7l6-4M2 7l6 4" stroke="#9fb3d6" stroke-width="2" fill="none"/>
  <path d="M38 7h26M64 7l-6-4M64 7l-6 4" stroke="#fff" stroke-width="2.5" fill="none"/>
</svg>
<div class="avatar" role="img" aria-label="Portrait photo of the client giving the testimonial"></div>
<svg class="abs" style="left:0;top:3150px" width="1200" height="52" viewBox="0 0 1200 52">
  <polygon points="0,52 0,20 1200,50 1200,52" fill="#fff"/>
</svg>

<h2 class="section-title" style="top:3278px">Latest Blog</h2>
<article class="blog-card" style="left:97px">
  <div class="blog-img" role="img" aria-label="Photo of a hand touching a glowing lead generation interface" style="background:linear-gradient(135deg,#0c2a4d,#2f79b5 55%,#0b1f3a)"></div>
  <div class="blog-meta"><span>Dec 03</span><span><svg width="12" height="10" viewBox="0 0 12 10"><ellipse cx="6" cy="4.5" rx="5.5" ry="4" fill="#fff"/></svg></span></div>
  <h3>Neque porro quisquam dolorem</h3>
  <p>It has survived not only five centuries, but also the leap into electronic typesetting,</p>
  <span class="more">Read More »</span>
</article>
<article class="blog-card" style="left:443px">
  <div class="blog-img" role="img" aria-label="Photo of paper figures and a magnet on a wooden table" style="background:linear-gradient(135deg,#5a3a22,#9a6b45 50%,#3b2616)"></div>
  <div class="blog-meta"><span>Dec 03</span><span><svg width="12" height="10" viewBox="0 0 12 10"><ellipse cx="6" cy="4.5" rx="5.5" ry="4" fill="#fff"/></svg></span></div>
  <h3>Porro quisquam est qui</h3>
  <p>It has survived not only five centuries, but also the leap into electronic typesetting,</p>
  <span class="more">Read More »</span>
</article>
<article class="blog-card" style="left:798px">
  <div class="blog-img" role="img" aria-label="Photo of a person typing on a laptop showing a lead generation screen" style="background:linear-gradient(135deg,#7a7f88,#c8ccd2 50%,#3d4048)"></div>
  <div class="blog-meta"><span>Dec 03</span><span><svg width="12" height="10" viewBox="0 0 12 10"><ellipse cx="6" cy="4.5" rx="5.5" ry="4" fill="#fff"/></svg></span></div>
  <h3>Dolorem ipsum quia dolor</h3>
  <p>It has survived not only five centuries, but also the leap into electronic typesetting,</p>
  <span class="more">Read More »</span>
</article>

<footer>
  <svg class="abs" style="left:0;top:3750px" width="1200" height="388" viewBox="0 0 1200 388">
    <polygon points="0,50 1200,0 1200,388 0,388" fill="#111"/>
    <polygon points="0,45 700,45 0,85" fill="#1e6fb8"/>
  </svg>
  <div class="social"><span></span><span></span><span></span><span></span></div>
  <div class="footer-brand">HALVERN</div>
  <div class="newsletter-label">JOIN OUR NEWSLETTER</div>
  <div class="newsletter">Email address<i></i></div>
  <nav class="footer-nav"><span>Home</span><span>About us</span><span>Services</span><span>Project</span><span>Blog</span><span>Contact</span></nav>
  <div class="copyright">Copyright © 2018, All Rights Reserved</div>
</footer>

</body>
</html>
```